Business Card Design and Logo Needed

I need Business Cards and a Logo for my website and public speaking business which can be found at: www.kelsa-thorn.example

I'm looking for creative and unique ideas. Some business cards I've found online that I like can be found at:
http://gigplatelo.example/general/18-smokin-hot-business-card-designs/

and at

http://www.vortaplume.example/2009/04/50-creative-business-cards-of-50-graphic-designers/

```html
<!DOCTYPE html>
<html lang="en">
<head>
<meta charset="utf-8">
<title>Kelsa Thorn – Business Card</title>
<link rel="stylesheet" href="https://fonts.googleapis.com/css2?family=Open+Sans:ital,wght@0,300;0,400;1,300;1,400;1,700&family=Raleway:wght@200&display=swap">
<style>
  :root {
    --page: #ffffff;
    --forest: #435a14;
    --forest-text: #4a5e1a;
    --tagline: #c9d3b3;
    --leaf: #6b8a22;
    --sage: #8f9c5c;
    --card-edge: #a4a97c;
  }
  * { margin: 0; padding: 0; box-sizing: border-box; }
  html, body {
    width: 1200px;
    height: 900px;
    overflow: hidden;
    background: var(--page);
    font-family: "Open Sans", Arial, sans-serif;
  }
  .canvas {
    position: relative;
    width: 1200px;
    height: 900px;
  }
  .card {
    position: absolute;
    left: 200px;
    width: 750px;
    height: 376px;
  }
  .card--front {
    top: 44px;
    background: var(--forest);
    border-top-left-radius: 100px;
  }
  .tagline {
    position: absolute;
    left: 40px;
    bottom: 26px;
    font-weight: 300;
    font-size: 26px;
    letter-spacing: 0.2px;
    color: var(--tagline);
  }
  .card--back {
    top: 484px;
    background: var(--page);
    border: 1.5px solid var(--card-edge);
    border-top-right-radius: 120px;
  }
  .identity {
    position: absolute;
    right: 53px;
    top: 82px;
    text-align: right;
  }
  .identity__name {
    font-family: "Raleway", "Helvetica Neue", sans-serif;
    font-weight: 200;
    font-size: 70px;
    line-height: 1;
    letter-spacing: 1px;
    color: var(--forest-text);
    text-transform: uppercase;
  }
  .identity__role {
    margin-top: 4px;
    font-style: italic;
    font-weight: 300;
    font-size: 20px;
    color: var(--sage);
  }
  .contact__phone {
    position: absolute;
    right: 53px;
    top: 252px;
    font-style: italic;
    font-weight: 700;
    font-size: 26px;
    color: var(--forest-text);
  }
  .contact__links {
    position: absolute;
    right: 53px;
    top: 298px;
    display: flex;
    gap: 44px;
    font-style: italic;
    font-weight: 400;
    font-size: 25px;
    color: var(--leaf);
  }
</style>
</head>
<body>
  <main class="canvas">
    <section class="card card--front" aria-label="Card front">
      <p class="tagline">wonder. explore. dream. achieve</p>
    </section>

    <section class="card card--back" aria-label="Card back">
      <div class="identity">
        <h1 class="identity__name">Kelsa Thorn</h1>
        <p class="identity__role">public speaker</p>
      </div>
      <p class="contact__phone">0100 555 014</p>
      <p class="contact__links">
        <span class="contact__email">kelsa@kelsa-thorn.example</span>
        <span class="contact__web">kelsa-thorn.example</span>
      </p>
    </section>
  </main>
</body>
</html>
```